Corporate Dinner Invitation – Bold, Professional Look with Subtle Arabic Flair

We are seeking a bold, professional invitation design for a VIP dinner event hosted by Torlan during the KQRW Summit on Friday, July 18th. This will be used primarily for LinkedIn promotion and as a PDF invitation shared directly with physicians, so it must look clean and polished in portrait orientation.
The design should reflect a high-end corporate aesthetic while still being eye-catching. We’d like to see a very subtle Arabic or Moroccan-inspired design element — think minimal patterns or shapes worked lightly into the background or border. This flair should feel tasteful and restrained, not thematic or decorative. If you need some inspiration for the arabic/morrocan theme - please look up the Zafrani Lounge website (https://www.zafranilo.com/).
Design Guidelines:
Portrait orientation only
Bold, clean, modern layout
Use of both Torlan and ORB Spine TQ brand colors preferred
Use of both Torlan and ORB Spine TQ logos (ORB Spine TQ logo is a subsidiary of the Torlan logo - so please make the Torlan logo the larger of the two; they are both the same company - Torlan owns ORB Spine TQ).
Strong, readable typography that looks professional and commands attention
Design must work well as both a LinkedIn graphic and a standalone PDF
Visual tone: corporate, high-level, medical, innovative
Event Details:
Date: Friday, July 18th
Time: 8:00pm - 10:00pm EST
Location: Zafrani Lounge (817 SE W Canal Rd, Miami, FL 33145)
Speakers: Gregory Lasko, MD; Calvin Brandt, MD; Suren Pathak, MD (I am including headshots of each speaker - they need to be included on the invite - please remove the backgrounds in the headshot to make all of them uniform looking on the invite)
Final Deliverables:
High-res PDF
PNG or JPEG preview for LinkedIn
Editable source file (Canva, AI or InDesign)
Target Market(s)
Physicians
Industry/Entity Type
Medical Device

```html
<!DOCTYPE html>
<html lang="en">
<head>
<meta charset="utf-8">
<title>VIP Dinner Invitation – Torlan</title>
<link rel="stylesheet" href="https://fonts.googleapis.com/css2?family=Urbanist:wght@400;500&display=swap">
<style>
  :root {
    --bg: #221e1f;
    --gold: #d9b862;
    --gold-light: #f3dc72;
    --gold-deep: #b8893a;
    --line: #9c8452;
    --white: #ffffff;
  }
  * { margin: 0; padding: 0; box-sizing: border-box; }
  html, body { width: 846px; height: 1200px; overflow: hidden; background: var(--bg); }
  .invite {
    position: relative;
    width: 846px;
    height: 1200px;
    background: var(--bg);
    font-family: "Urbanist", sans-serif;
    color: var(--gold);
    overflow: hidden;
  }
  .frame { position: absolute; inset: 0; }
  .corner-ornament {
    position: absolute;
    width: 195px;
    height: 195px;
    opacity: 0.55;
  }
  .corner-ornament.top-left { top: 0; left: 0; background: radial-gradient(circle at 0 0, rgba(156,132,82,0.35), rgba(156,132,82,0) 70%); }
  .corner-ornament.top-right { top: 0; right: 0; background: radial-gradient(circle at 100% 0, rgba(156,132,82,0.35), rgba(156,132,82,0) 70%); }
  .corner-ornament.bottom-left { bottom: 0; left: 0; background: radial-gradient(circle at 0 100%, rgba(156,132,82,0.35), rgba(156,132,82,0) 70%); }
  .corner-ornament.bottom-right { bottom: 0; right: 0; background: radial-gradient(circle at 100% 100%, rgba(156,132,82,0.35), rgba(156,132,82,0) 70%); }

  .title {
    position: absolute;
    left: 0; right: 0;
    top: 200px;
    text-align: center;
    font-weight: 400;
    font-size: 76px;
    line-height: 80px;
    letter-spacing: 1px;
    background: linear-gradient(180deg, var(--gold-light) 0%, var(--gold) 55%, var(--gold-deep) 100%);
    -webkit-background-clip: text;
    background-clip: text;
    color: transparent;
  }
  .event-details {
    position: absolute;
    left: 0; right: 0;
    top: 378px;
    text-align: center;
    font-size: 21.5px;
    line-height: 34px;
    text-transform: uppercase;
    letter-spacing: 0.2px;
  }
  .speakers {
    position: absolute;
    left: 0; right: 0;
    top: 494px;
    text-align: center;
    font-size: 18px;
    line-height: 28px;
  }
  .speaker-photos {
    position: absolute;
    left: 146px;
    top: 627px;
    width: 562px;
    height: 324px;
    background:
      linear-gradient(180deg, rgba(34,30,31,0) 70%, var(--bg) 100%),
      linear-gradient(90deg, #34436e 0%, #3f4f7e 38%, #d9dde3 48%, #eef0f2 70%, #e6e7ea 92%, rgba(34,30,31,0.6) 100%);
    border-radius: 160px 160px 0 0 / 120px 120px 0 0;
    opacity: 0.9;
  }
  .brand-lockup {
    position: absolute;
    left: 0; right: 0;
    top: 994px;
    display: flex;
    justify-content: center;
    align-items: baseline;
    gap: 14px;
    color: var(--white);
  }
  .brand-primary { font-size: 30px; font-weight: 500; letter-spacing: 1px; }
  .brand-secondary { font-size: 18px; font-weight: 500; letter-spacing: 1px; }
</style>
</head>
<body>
<main class="invite">
  <div class="corner-ornament top-left" role="img" aria-label="Fine gold arabesque corner ornament"></div>
  <div class="corner-ornament top-right" role="img" aria-label="Fine gold arabesque corner ornament"></div>
  <div class="corner-ornament bottom-left" role="img" aria-label="Fine gold arabesque corner ornament"></div>
  <div class="corner-ornament bottom-right" role="img" aria-label="Fine gold arabesque corner ornament"></div>

  <svg class="frame" width="846" height="1200" viewBox="0 0 1620 2296" preserveAspectRatio="none" aria-hidden="true">
    <polygon fill="none" stroke="var(--line)" stroke-width="1.6"
      points="808,110 1073,322 1353,322 1353,545 1473,640 1473,1655 1353,1750 1353,1975 1073,1975 808,2185 548,1975 265,1975 265,1750 147,1655 147,640 265,545 265,322 548,322"/>
  </svg>

  <h1 class="title">VIP<br>DINNER</h1>

  <div class="event-details">
    <p>Friday, July 18th</p>
    <p>8:00pm - 10:00pm EST</p>
    <p>At Zafrani Lounge, 817 SE W Canal Rd, Miami, FL 33145</p>
  </div>

  <div class="speakers">
    <p>Speakers:</p>
    <p>Gregory Lasko, MD; Calvin Brandt, MD; Suren Pathak, MD</p>
  </div>

  <div class="speaker-photos" role="img" aria-label="Headshots of the three speakers, Gregory Lasko, Calvin Brandt and Suren Pathak, with backgrounds removed"></div>

  <div class="brand-lockup">
    <span class="brand-primary">TORLAN</span>
    <span class="brand-secondary">ORB SPINE TQ</span>
  </div>
</main>
</body>
</html>
```